VS Business Card

Design new business cards for VELNOsys

Please see attached for the design brief

**** Please note, please feel free to propose a font that works for a professional, technology company ***

Target Market(s)

Technology buyers

Industry/Entity Type

Business

```html
<!DOCTYPE html>
<html lang="en">
<head>
<meta charset="utf-8">
<title>VELNOsys Business Card</title>
<link rel="stylesheet" href="https://fonts.googleapis.com/css2?family=Jost:wght@400;500;600&family=Michroma&display=swap">
<style>
  :root {
    --navy: #22356b;
    --orange: #f3a53a;
    --paper: #ffffff;
    --backdrop: #786b69;
    --ink-light: #ffffff;
  }
  * { margin: 0; padding: 0; box-sizing: border-box; }
  html, body { width: 1200px; height: 803px; overflow: hidden; }
  body {
    background: var(--backdrop);
    font-family: "Jost", sans-serif;
    position: relative;
  }
  .card {
    position: absolute;
    top: 68px;
    width: 429px;
    height: 275px;
    background: var(--paper);
    overflow: hidden;
  }
  .card--front { left: 122px; }
  .card--back { left: 656px; }

  /* Front */
  .front-panel {
    position: absolute; left: 0; top: 0; width: 100%; height: 212px;
    background: var(--navy);
  }
  .tagline {
    position: absolute; color: var(--orange); font-weight: 400; white-space: nowrap;
  }
  .card--front .tagline { left: 200px; top: 24px; font-size: 16px; }
  .person-name {
    position: absolute; left: 245px; top: 54px;
    font-family: "Michroma", sans-serif; font-size: 16px; color: var(--ink-light);
    letter-spacing: 0.5px; font-weight: 400;
  }
  .person-role {
    position: absolute; left: 247px; top: 80px; font-size: 13px; color: var(--ink-light);
  }
  .contact-list {
    position: absolute; left: 30px; top: 112px; list-style: none; color: var(--ink-light);
    font-size: 12px;
  }
  .contact-list li { display: flex; align-items: center; height: 17px; margin-bottom: 1px; }
  .contact-list li.contact--email { font-size: 10.5px; margin-top: 2px; }
  .contact-icon { width: 11px; height: 11px; margin-right: 5px; fill: var(--ink-light); }
  .brand {
    position: absolute; display: flex; align-items: center; color: var(--navy);
    font-weight: 500; white-space: nowrap;
  }
  .brand-square { background: var(--navy); display: block; }
  .card--front .brand { left: 32px; top: 226px; font-size: 22px; }
  .card--front .brand-square { width: 12px; height: 12px; margin-right: 7px; }

  /* Back */
  .card--back .tagline { left: 0; width: 100%; text-align: center; top: 16px; font-size: 19px; }
  .card--back .brand { left: 0; width: 100%; justify-content: center; top: 70px; font-size: 54px; }
  .card--back .brand-square { width: 28px; height: 28px; margin-right: 14px; }
  .address-band {
    position: absolute; left: 0; top: 186px; width: 100%; height: 48px;
    background: var(--navy); color: var(--ink-light); text-align: center;
    font-size: 12px; line-height: 18px; padding-top: 6px;
  }
</style>
</head>
<body>
  <section class="card card--front" aria-label="Business card front">
    <div class="front-panel"></div>
    <p class="tagline">...Progress Is Our Purpose</p>
    <h1 class="person-name">Martin Halek</h1>
    <p class="person-role">CEO</p>
    <ul class="contact-list">
      <li><svg class="contact-icon" viewBox="0 0 12 12" aria-hidden="true"><path d="M3 1l2 2.5-1 1.2c.6 1.3 1.7 2.4 3 3l1.2-1L11 9l-1.3 2C5.5 11 1 6.5 1 2.3z"/></svg>+41440000210</li>
      <li><svg class="contact-icon" viewBox="0 0 12 12" aria-hidden="true"><path d="M3 1l2 2.5-1 1.2c.6 1.3 1.7 2.4 3 3l1.2-1L11 9l-1.3 2C5.5 11 1 6.5 1 2.3z"/></svg>+41440000211</li>
      <li><svg class="contact-icon" viewBox="0 0 12 12" aria-hidden="true"><path d="M3 1h5v3H3zM1 5h10v5H9V8H3v2H1zM3 9h6v2H3z"/></svg>+41800000390</li>
      <li><svg class="contact-icon" viewBox="0 0 12 12" aria-hidden="true"><path d="M3.5 0.5h5v11h-5zM4.5 1.5v7h3v-7z"/></svg>+41 790000457</li>
      <li class="contact--email"><svg class="contact-icon" viewBox="0 0 12 12" aria-hidden="true"><path d="M1 3h10v7H1zM1.8 3.6L6 7l4.2-3.4v-.1H1.8z"/></svg>martin.halek@velnosys-it.com</li>
    </ul>
    <div class="brand"><span class="brand-square"></span>VELNOsys</div>
  </section>

  <section class="card card--back" aria-label="Business card back">
    <p class="tagline">...Progress Is Our Purpose</p>
    <div class="brand"><span class="brand-square"></span>VELNOsys</div>
    <div class="address-band">
      <p>VELNOsys Solutions AG,&nbsp; Seefeldweg 22, 8712 Stäfa, Switzerland</p>
      <p>http://www.velnosys-it.com</p>
    </div>
  </section>
</body>
</html>
```